Keystone Prime Water Tank

I primarily market the water tanks so want a business care that reflects that. I have attached the water tank logo. You have been working on our water tank so maybe we can use that on the card et. I am leaving as one sided but can be double sided if that works. The information that needs to be on the cards is as follows: Gerald T. Munro Phone numbers: Office 555-284-9137 Direct 555-619-2405 Mobile 555-372-5841 email address: gerald@fieldgearworks.com Address P.O. Box 8273 Larkmoor, NC 30512 Web Page: www.fieldgearworks.com. A lot to fit on the card. Thanks

```html
<!DOCTYPE html>
<html lang="en">
<head>
<meta charset="utf-8">
<title>Keystone Prime Water Tank – Business Cards</title>
<link rel="stylesheet" href="https://fonts.googleapis.com/css2?family=Poppins:wght@400;500;600;700&display=swap">
<style>
  :root {
    --brand-red: #e51921;
    --ink: #111111;
    --paper: #ffffff;
    --canvas: #ffffff;
    --shadow: rgba(0, 0, 0, 0.38);
  }
  * { margin: 0; padding: 0; box-sizing: border-box; }
  html, body {
    width: 1200px; height: 1200px; overflow: hidden;
    background: var(--canvas);
    font-family: "Poppins", sans-serif;
  }
  .stage { position: relative; width: 1200px; height: 1200px; }

  .card {
    position: absolute; overflow: hidden;
    box-shadow: 6px 7px 10px var(--shadow);
  }

  /* Horizontal front */
  .card--front {
    left: 97px; top: 272px; width: 533px; height: 306px;
    border-radius: 31px; background: var(--paper);
  }
  .front-band {
    position: absolute; left: 0; bottom: 0; width: 100%; height: 34px;
    background: var(--brand-red);
  }
  .front-tab {
    position: absolute; left: 119px; top: 250px; width: 296px; height: 24px;
  }
  .front-url {
    position: absolute; left: 0; right: 0; top: 259px;
    text-align: center; color: var(--paper);
    font-size: 17px; font-weight: 400; letter-spacing: 0.2px;
  }

  .wordmark { position: absolute; text-align: center; color: var(--ink); font-weight: 700; }
  .wordmark__square { display: block; margin: 0 auto; background: var(--brand-red); }
  .wordmark__name { display: block; line-height: 1.1; text-transform: uppercase; }

  .card--front .wordmark { left: 0; right: 0; top: 66px; }
  .card--front .wordmark__square { width: 44px; height: 44px; margin-bottom: 14px; }
  .card--front .wordmark__name { font-size: 27px; }

  /* Horizontal back */
  .card--back {
    left: 97px; top: 637px; width: 533px; height: 305px;
    border-radius: 31px; background: var(--brand-red); color: var(--paper);
  }
  .card--back .person-name {
    position: absolute; left: 45px; top: 43px;
    font-size: 37px; font-weight: 600; letter-spacing: 0.3px;
  }
  .card--back .contact-list { position: absolute; left: 44px; top: 173px; }
  .card--back .contact-item { height: 19.3px; font-size: 13.5px; }
  .card--back .contact-item svg { width: 11px; height: 11px; margin-right: 9px; }
  .card--back .wordmark {
    right: 36px; top: 180px; width: 150px; color: var(--paper);
  }
  .card--back .wordmark__square { width: 28px; height: 28px; background: var(--paper); margin-bottom: 8px; }
  .card--back .wordmark__name { font-size: 15px; }

  .divider {
    position: absolute; left: 678px; top: 266px; width: 1px; height: 675px;
    background: var(--brand-red);
  }

  /* Vertical card */
  .card--vertical {
    left: 717px; top: 259px; width: 394px; height: 690px;
    border-radius: 44px; background: var(--paper);
  }
  .vertical-panel {
    position: absolute; left: 0; top: 324px; width: 100%; bottom: 0;
    background: var(--brand-red); color: var(--paper);
  }
  .card--vertical .wordmark { left: 0; right: 0; top: 78px; }
  .card--vertical .wordmark__square { width: 56px; height: 56px; margin-bottom: 18px; }
  .card--vertical .wordmark__name { font-size: 31px; }
  .card--vertical .person-name {
    position: absolute; left: 44px; top: 60px;
    font-size: 36px; font-weight: 600; letter-spacing: 0.3px;
  }
  .card--vertical .contact-list { position: absolute; left: 43px; top: 159px; }
  .card--vertical .contact-item { height: 24.6px; font-size: 17.5px; }
  .card--vertical .contact-item svg { width: 14px; height: 14px; margin-right: 12px; }

  .contact-list { list-style: none; }
  .contact-item { display: flex; align-items: center; white-space: nowrap; font-weight: 400; }
  .contact-item svg { flex: none; }
</style>
</head>
<body>
<svg width="0" height="0" style="position:absolute" aria-hidden="true">
  <defs>
    <symbol id="icon-phone" viewBox="0 0 20 20">
      <circle cx="10" cy="10" r="10" fill="#fff"/>
      <path d="M6.4 5.2l1.7-.4 1 2.4-1.1.9a6 6 0 0 0 2.9 2.9l.9-1.1 2.4 1-.4 1.7c-3.9.5-8.2-3.8-7.4-7.4z" fill="#e51921"/>
    </symbol>
    <symbol id="icon-direct" viewBox="0 0 20 20">
      <circle cx="10" cy="10" r="10" fill="#fff"/>
      <path d="M6.2 5.4l1.6-.4.9 2.2-1 .8a5.4 5.4 0 0 0 2.6 2.6l.8-1 2.2.9-.4 1.6c-3.6.5-7.4-3.3-6.7-6.7z" fill="#e51921"/>
      <path d="M11 5.2h3.2v3.2" fill="none" stroke="#e51921" stroke-width="1.3"/>
    </symbol>
    <symbol id="icon-mobile" viewBox="0 0 20 20">
      <circle cx="10" cy="10" r="10" fill="#fff"/>
      <rect x="7" y="4.8" width="6" height="10.4" rx="1.2" fill="none" stroke="#e51921" stroke-width="1.3"/>
      <circle cx="10" cy="13.3" r=".7" fill="#e51921"/>
    </symbol>
    <symbol id="icon-mail" viewBox="0 0 20 20">
      <circle cx="10" cy="10" r="10" fill="#fff"/>
      <rect x="5" y="6.5" width="10" height="7" rx=".8" fill="#e51921"/>
      <path d="M5.4 7l4.6 3.6L14.6 7" fill="none" stroke="#fff" stroke-width="1"/>
    </symbol>
    <symbol id="icon-pin" viewBox="0 0 20 20">
      <circle cx="10" cy="10" r="10" fill="#fff"/>
      <path d="M10 4.4a3.4 3.4 0 0 0-3.4 3.4c0 2.5 3.4 6 3.4 6s3.4-3.5 3.4-6A3.4 3.4 0 0 0 10 4.4z" fill="#e51921"/>
      <circle cx="10" cy="7.8" r="1.2" fill="#fff"/>
      <path d="M6.5 15.2h7" stroke="#e51921" stroke-width="1.2"/>
    </symbol>
    <symbol id="icon-web" viewBox="0 0 20 20">
      <circle cx="10" cy="10" r="10" fill="#fff"/>
      <circle cx="10" cy="10" r="5" fill="none" stroke="#e51921" stroke-width="1.2"/>
      <ellipse cx="10" cy="10" rx="2" ry="5" fill="none" stroke="#e51921" stroke-width="1"/>
      <path d="M5 10h10" stroke="#e51921" stroke-width="1"/>
    </symbol>
  </defs>
</svg>

<main class="stage">
  <section class="card card--front" aria-label="Business card front">
    <div class="wordmark">
      <span class="wordmark__square"></span>
      <span class="wordmark__name">Keystone Prime</span>
      <span class="wordmark__name">Water Tank</span>
    </div>
    <div class="front-band"></div>
    <svg class="front-tab" viewBox="0 0 296 24" preserveAspectRatio="none" aria-hidden="true">
      <polygon points="0,24 22,0 274,0 296,24" fill="var(--brand-red)"/>
    </svg>
    <p class="front-url">www.fieldgearworks.com</p>
  </section>

  <section class="card card--back" aria-label="Business card back">
    <h1 class="person-name">Gerald T. Munro</h1>
    <ul class="contact-list">
      <li class="contact-item"><svg><use href="#icon-phone"/></svg>555-284-9137</li>
      <li class="contact-item"><svg><use href="#icon-direct"/></svg>555-619-2405</li>
      <li class="contact-item"><svg><use href="#icon-mobile"/></svg>Mobile 555-372-5841</li>
      <li class="contact-item"><svg><use href="#icon-mail"/></svg>gerald@fieldgearworks.com</li>
      <li class="contact-item"><svg><use href="#icon-pin"/></svg>P.O. Box 8273 Larkmoor, NC 30512</li>
    </ul>
    <div class="wordmark">
      <span class="wordmark__square"></span>
      <span class="wordmark__name">Keystone Prime</span>
      <span class="wordmark__name">Water Tank</span>
    </div>
  </section>

  <div class="divider"></div>

  <section class="card card--vertical" aria-label="Vertical business card">
    <div class="wordmark">
      <span class="wordmark__square"></span>
      <span class="wordmark__name">Keystone Prime</span>
      <span class="wordmark__name">Water Tank</span>
    </div>
    <div class="vertical-panel">
      <h2 class="person-name">Gerald T. Munro</h2>
      <ul class="contact-list">
        <li class="contact-item"><svg><use href="#icon-phone"/></svg>555-284-9137</li>
        <li class="contact-item"><svg><use href="#icon-direct"/></svg>555-619-2405</li>
        <li class="contact-item"><svg><use href="#icon-mobile"/></svg>Mobile 555-372-5841</li>
        <li class="contact-item"><svg><use href="#icon-mail"/></svg>gerald@fieldgearworks.com</li>
        <li class="contact-item"><svg><use href="#icon-pin"/></svg>P.O. Box 8273 Larkmoor, NC 30512</li>
        <li class="contact-item"><svg><use href="#icon-web"/></svg>www.fieldgearworks.com</li>
      </ul>
    </div>
  </section>
</main>
</body>
</html>
```